Website Design for a DJ Entertainment and Productions Comany

We are a full service DJ Entertainment and Productions company looking to have a strong presence in our local market and need a phenomenal website design to drive clients to the site but then also keep them there. We cater to all types of different events varying from weddings to proms to corporate events, birthdays, bar mitzvah's and so on and so on. We also do full lighting for any type of event and we also offer a photobooth service for various events. The best way to get an idea of the services that we offer is to visit http://www.velmorahaus.com/index.html This site is NOT our own but only linked as an example of what we do and will give you an overall overview of what we offer.
We are looking for pure creativity as there are multiple facets to our company and the services we offer. On the one hand we can provide a night club party atmosphere for Proms or dances but on the other hand we also provide professional full service emcee/DJ for weddings and formal events. The key for this site would be to have the pages for each category match the look and feel of the actual service provided, ie the Wedding page will look more refined and professional vs the Party DJ page. Each page needs to fit the overall feel of the Company and Logo though. Here is a list of pages that we would need to have on the final site.
HOME PAGE
PROFESSINAL DJS- This will have info. and pricing of our DJ services for everything but weddings. Should have pics and videos somewhere on this page.
WEDDINGS- All wedding package pricing and info. This page should look more elegant, formal and high class compared to the other pages.
PHOTOBOOTH-Page with info, pricing on photobooth see http://www.glintrivuphotobooth.com/
LIGHTING DESIGN-Info on our lighting services along with pricing
CORPORATE EVENTS-Info on services and pricing for corporate events. This page should seem more professional centered towards business clientele.
CLIENT LOGIN-Page for existing clients to logon to update info and fill out information.
CONNECT WITH US- Social Media links.
Our logo was submitted through Pixel Harbor but I am open to suggestions on revisions if you feel the need to change it. Color is also not set in stone.
I have increased my budget $200 more. Please submit your designs for review, deadline is approaching quickly. Also see brief for revisions.
Thank you.
Target Market(s)
Broad Range but usually Under 40
Industry/Entity Type
Night Club
Look and feel

```html
<!DOCTYPE html>
<html lang="en">
<head>
<meta charset="utf-8">
<title>Nova Pulse Entertainment &amp; Productions</title>
<link rel="stylesheet" href="https://fonts.googleapis.com/css2?family=Arimo:wght@400;700&family=Roboto+Condensed:wght@700&display=swap">
<style>
:root{
  --red:#e01212;
  --red-dark:#7a0a0a;
  --red-deep:#3a0404;
  --maroon:#5a0606;
  --black:#000;
  --white:#fff;
  --yellow:#ffd21a;
  --ink:#1e2a44;
  --magenta:#c40fa8;
  --green:#0c4a14;
  --blue:#2b35c8;
  --grey-card:#e9e9e9;
}
*{box-sizing:border-box;margin:0;padding:0}
html,body{width:1064px;height:1200px;overflow:hidden}
body{position:relative;background:var(--black);font-family:"Arimo",Arial,sans-serif;color:var(--ink)}
.abs{position:absolute}

.site-header{left:0;top:0;width:1064px;height:522px;
  background:radial-gradient(ellipse at 50% 30%,#6a0808 0%,var(--red-deep) 55%,#1a0202 100%)}
.top-strip{left:0;top:0;width:1064px;height:10px;background:var(--red-dark)}
.login-bar{left:648px;top:0;width:356px;height:38px;background:var(--maroon);border:1px solid #a01010;border-top:0;border-radius:0 0 10px 10px;display:flex;align-items:center;gap:6px;padding:0 6px}
.login-field{width:134px;height:24px;border-radius:12px;background:linear-gradient(#fff,#ddd);font-size:12px;color:#888;padding:5px 12px}
.login-go{margin-left:6px;width:56px;height:26px;border-radius:13px;background:linear-gradient(#ff2a2a,#b00000);color:#fff;font-weight:700;font-size:13px;text-align:center;line-height:26px}

.brand{left:68px;top:22px;display:flex;align-items:center;gap:14px}
.brand-dot{width:74px;height:74px;border-radius:50%;background:var(--red)}
.brand-name{font-weight:700;font-size:46px;line-height:46px;color:var(--red);letter-spacing:1px}
.brand-sub{font-weight:700;font-size:11px;color:var(--red);letter-spacing:.3px;margin-top:4px}

.tagline{left:397px;top:62px;font-size:19px;line-height:23px;color:#eee;letter-spacing:.5px}
.tagline b{display:block;color:var(--yellow);margin-left:112px;letter-spacing:1px}

.call-box{left:777px;top:56px;width:226px;height:56px;border-radius:6px;background:linear-gradient(#ff3030,#b00000);display:flex;align-items:center;padding-left:12px;gap:14px;color:#fff}
.call-label{font-size:13px;font-weight:700;line-height:14px}
.call-number{font-size:23px;font-weight:700;line-height:26px}

.main-nav{left:32px;top:131px;width:981px;height:42px;border-radius:8px;background:linear-gradient(#c30c0c,#7a0303);display:flex;align-items:center;padding-left:18px}
.main-nav span{color:#fff;font-weight:700;font-size:13px;padding:0 12px;height:48px;line-height:48px;margin-top:-6px}
.main-nav .is-active{background:var(--red)}

.hero{left:32px;top:193px;width:980px;height:306px;border:1px solid #ccc;border-radius:3px;
  background:linear-gradient(100deg,#d9c3d6 0%,#6c3f6a 25%,#3a2b5c 45%,#8a4a6e 62%,#c9b0c9 82%,#eceaf2 100%)}
.hero-list{right:13px;top:130px;text-align:right;font-weight:700;font-size:17px;line-height:27px}
.hero-list li{list-style:none}
.cta{left:788px;top:457px;width:234px;height:42px}
.cta span{position:absolute;left:30px;top:0;line-height:42px;color:#fff;font-weight:700;font-size:16px}

.content{left:0;top:522px;width:1064px;height:553px;background:var(--white)}
.welcome-title{left:31px;top:539px;font-weight:700;font-size:19.5px;color:#d10a0a}
.welcome-copy{left:31px;top:577px;width:666px;font-size:12px;line-height:16px;text-align:justify;color:var(--ink)}
.welcome-copy p{margin-bottom:22px}
.welcome-copy p + p + p{margin-top:16px}
.read-more{left:613px;top:820px;font-weight:700;font-size:13px;color:#a00;border-bottom:1px solid #a00}

.events{left:734px;top:542px;width:278px;height:297px;border:1px solid #e8cdd0;background:linear-gradient(90deg,#fbeeee,#fff 20%,#fff 80%,#fbeeee)}
.events-title{position:absolute;left:17px;top:12px;font-weight:700;font-size:16px;color:#111}
.event{position:absolute;left:18px;width:250px;height:68px}
.event-thumb{position:absolute;left:0;top:0;width:82px;height:66px;border:1px solid #c43;background:linear-gradient(135deg,#2c2a6e,#a24b8c 50%,#3a1a40)}
.event-text{position:absolute;left:92px;top:0;width:160px;font-size:12px;line-height:16px;color:#111}
.event-more{position:absolute;right:0;top:46px;font-weight:700;font-size:13px;color:#111}

.services{left:31px;top:850px;width:981px;height:210px;background:var(--black)}
.services-icon{position:absolute;left:12px;top:14px}
.services-title{position:absolute;left:70px;top:16px;font-family:"Roboto Condensed",Arial Narrow,sans-serif;font-size:24px;color:var(--yellow)}
.services-note{position:absolute;right:12px;top:25px;font-weight:700;font-size:13px;color:#eee}
.service-card{position:absolute;top:61px;width:183px;height:138px;border:4px solid #8a8a8a;border-radius:4px;background:var(--white);overflow:hidden}
.service-photo{height:80px}
.service-name{font-family:"Roboto Condensed",Arial Narrow,sans-serif;font-size:20px;text-align:center;line-height:24px;margin-top:2px}
.service-link{text-align:center;font-size:13px;color:#111;margin-top:2px}

.footer-band{left:0;top:1075px;width:1064px;height:61px;background:linear-gradient(#2a2a2a,#0c0c0c)}
.footer-nav{left:24px;top:1082px;width:1000px;height:49px;background:linear-gradient(100deg,#a80000,#e83a1a 45%,#b30000 70%,#8a0000);display:flex;align-items:center;padding-left:18px}
.footer-nav span{color:#fff;font-size:10.5px;margin-right:18px}
.footer-connect{position:absolute;right:136px;top:16px;color:#fff;font-weight:700;font-size:13px}
.social{position:absolute;top:11px;width:22px;height:22px;border-radius:50%;background:#fff}
.copyright{left:0;top:1136px;width:1064px;height:64px;background:linear-gradient(#111,#000);color:#fff;font-size:12.5px;text-align:center;padding-top:15px}
</style>
</head>
<body>

<header class="site-header abs">
  <div class="top-strip abs"></div>
  <div class="login-bar abs">
    <div class="login-field">User Name</div>
    <div class="login-field">Password</div>
    <div class="login-go">GO</div>
  </div>

  <div class="brand abs">
    <div class="brand-dot"></div>
    <div>
      <div class="brand-name">NOVA PULSE</div>
      <div class="brand-sub">ENTERTAINMENT &amp; PRODUCTIONS</div>
    </div>
  </div>

  <div class="tagline abs">PROFESSIONAL DJ'S FOR ALL YOUR<b>SPECIAL OCCASION...</b></div>

  <div class="call-box abs">
    <svg width="26" height="36" viewBox="0 0 26 36" aria-hidden="true">
      <path d="M6 2 L11 2 L13 10 L9 12 Q10 22 16 26 L19 22 L25 26 L23 33 Q14 35 6 24 Q0 12 6 2Z" fill="#fff"/>
    </svg>
    <div>
      <div class="call-label">Call Us :</div>
      <div class="call-number">01632 960 418</div>
    </div>
  </div>

  <nav class="main-nav abs">
    <span>PROFESSIONAL DJS</span>
    <span class="is-active">WEDDINGS</span>
    <span>PHOTOBOOTH</span>
    <span>LIGHTING DESIGN</span>
    <span>CORPORATE EVENTS</span>
    <span>CLIENT LOGIN</span>
    <span>CONNECT WITH US</span>
  </nav>

  <div class="hero abs" role="img" aria-label="Photo of a singer with a microphone and a crowd of party guests dancing under club lights">
    <ul class="hero-list abs">
      <li style="color:#111">PROFESSIONAL DJ</li>
      <li style="color:var(--magenta)">WEDDING PARTY</li>
      <li style="color:var(--green)">PHOTOBOOTH</li>
      <li style="color:var(--red)">LIGHTING DESIGN</li>
      <li style="color:var(--blue)">CORPORATE EVENTS</li>
    </ul>
  </div>
  <div class="cta abs">
    <svg width="234" height="42" viewBox="0 0 234 42" aria-hidden="true">
      <path d="M0 21 L20 0 H234 V42 H20 Z" fill="#b80000"/>
    </svg>
    <span>BOOK YOUR DJ TODAY</span>
  </div>
</header>

<main class="content abs"></main>
<h1 class="welcome-title abs">WELCOME TO NOVA PULSE ENTERTAINMENT &amp; PRODUCTIONS</h1>
<div class="welcome-copy abs">
  <p>Lorem ipsum dolor sit amet, consectetur adipiscing elit. Aliquam tincidunt mi id libero egestas ut interdum nibh cursus. Nulla erat orci, adipiscing vel molestie ac, vehicula in dui. Proin vel lorem in tellus placerat eleifend. Duis iaculis lorem a ipsum euismod vel ullamcorper arcu placerat. Aenean elementum tortor vel nisi bibendum bibendum. Aliquam fringilla feugiat a</p>
  <p>Lorem ipsum dolor sit amet, consectetur adipiscing elit. Aliquam tincidunt mi id libero egestas ut interdum nibh cursus. Nulla erat orci, gilla. Lorem ipsum dolor sit amet, consectetur adipiscing elit. Aliquam tincidunt mi id libero egestas ut interdum nibh cursus. Nulla erat orci, gilla.</p>
  <p>Lorem ipsum dolor sit amet, consectetur adipiscing elit. Aliquam tincidunt mi id libero egestas ut interdum nibh cursus. Nulla erat orci, gilla. Lorem ipsum dolor sit amet, consectetur adipiscing elit. Aliquam tincidunt mi id libero egestas ut interdum nibh cursus. Nulla erat orci, gilla.</p>
</div>
<div class="read-more abs">Read More &gt;</div>

<aside class="events abs">
  <div class="events-title">OUR LETEST EVENTS...</div>
  <div class="event" style="top:41px">
    <div class="event-thumb" role="img" aria-label="Event photo of a singer performing"></div>
    <div class="event-text">Lorem ipsum dolor sit amet, consectetur adipisc-ing Lorem</div>
    <div class="event-more">More...</div>
  </div>
  <div class="event" style="top:128px">
    <div class="event-thumb" role="img" aria-label="Event photo of a singer performing"></div>
    <div class="event-text">Lorem ipsum dolor sit amet, consectetur adipisc-ing Lorem</div>
    <div class="event-more">More...</div>
  </div>
  <div class="event" style="top:215px">
    <div class="event-thumb" role="img" aria-label="Event photo of a singer performing"></div>
    <div class="event-text">Lorem ipsum dolor sit amet, consectetur adipisc-ing Lorem</div>
    <div class="event-more">More...</div>
  </div>
</aside>

<section class="services abs">
  <svg class="services-icon" width="40" height="40" viewBox="0 0 40 40" aria-hidden="true">
    <circle cx="20" cy="20" r="18" fill="#f0a020"/>
    <path d="M20 20 L20 2 A18 18 0 0 1 37 25 Z" fill="#2e9b2e"/>
    <path d="M20 20 L37 25 A18 18 0 0 1 8 34 Z" fill="#d81818"/>
  </svg>
  <h2 class="services-title">OUR ALL PROFESSIONAL SERVICES</h2>
  <div class="services-note">Click below our service for complete information &amp; price list</div>

  <div class="service-card" style="left:12px">
    <div class="service-photo" role="img" aria-label="Photo of a DJ with headphones under purple lights" style="background:linear-gradient(135deg,#3a3ac0,#b04ad0 50%,#f070c0)"></div>
    <div class="service-name" style="color:#1a2a9a">PROFEESIONAL DJ</div>
    <div class="service-link">CLICK HERE &nbsp;DETAILS</div>
  </div>
  <div class="service-card" style="left:206px">
    <div class="service-photo" role="img" aria-label="Photo of a wedding reception table with flowers" style="background:linear-gradient(135deg,#e8ddc8,#f4ecdf 50%,#c86a5a)"></div>
    <div class="service-name" style="color:#9a1aa0">WEDDINGS</div>
    <div class="service-link">CLICK HERE &nbsp;DETAILS</div>
  </div>
  <div class="service-card" style="left:399px">
    <div class="service-photo" role="img" aria-label="Photo of friends posing in a photobooth" style="background:linear-gradient(135deg,#4a3a30,#c89080 50%,#d8c0b0)"></div>
    <div class="service-name" style="color:#0c6a14">PHOTOBOOTH</div>
    <div class="service-link">CLICK HERE &nbsp;DETAILS</div>
  </div>
  <div class="service-card" style="left:593px">
    <div class="service-photo" role="img" aria-label="Photo of a ballroom lit in pink and purple" style="background:linear-gradient(135deg,#4a1a3a,#a04a7a 50%,#d0a0c0)"></div>
    <div class="service-name" style="color:#d01010">LIGHTING DESIGN</div>
    <div class="service-link">CLICK HERE &nbsp;DETAILS</div>
  </div>
  <div class="service-card" style="left:787px">
    <div class="service-photo" role="img" aria-label="Photo of a microphone at a corporate conference" style="background:linear-gradient(135deg,#c8a070,#e8e0d8 50%,#9a9aa0)"></div>
    <div class="service-name" style="color:#333">CORPORATE EVENTS</div>
    <div class="service-link">CLICK HERE &nbsp;DETAILS</div>
  </div>
</section>

<footer>
  <div class="footer-band abs"></div>
  <nav class="footer-nav abs">
    <span>Professional DjS</span>
    <span>WEDDINGS</span>
    <span>PHOTOBOOTH</span>
    <span>LIGHTING DESIGN</span>
    <span>CORPORATE EVENTS</span>
    <span>CLIENT LOGIN</span>
    <span>CONNECT WITH US</span>
    <div class="footer-connect">CONNET WITH US</div>
    <div class="social" style="left:879px" aria-label="Social link"></div>
    <div class="social" style="left:916px" aria-label="Social link"></div>
    <div class="social" style="left:952px" aria-label="Social link"></div>
  </nav>
  <div class="copyright abs">Copyright Text</div>
</footer>

</body>
</html>
```